I need a business card representing my company, VELDAR, it's an artist management and design company. Complete name is "VELDAR Artist Mgmt. + Design Co." I need it to be world class and very appealing, sophisticated and artistically unique.
Updates

Posted an updated Brief please see. I need a business card representing my company, VELDAR, it's an artist management and design company. Complete name is "VELDAR Artist Mgmt. + Design Co." I need it to be world class and very appealing, sophisticated and artistically unique.

Designs look the same

Designs look the same

Target Market(s)

Advertisers, Entertainment Companies, Commercial companies

Industry/Entity Type

Advertising

Contact Information for Business Card

I need a business card representing my company, VELDAR, it's an artist management and design company. Complete name is "VELDAR Artist Mgmt. + Design Co." I need it to be world class and very appealing, sophisticated and artistically unique. One side can be VELDAR Artist Mgmt. + Design Co. and the other my name, Theodore Quillan, my contact telephone: 415.638.2097, email veldarartist@mailnest.example, my address: 2416 Harrowgate Ave. #317 Miami, FL 33152

Font styles to use
Other font styles liked:
• Calibri

Colors
ffffff
0455a3
f37122

Requirements
Must have
• "VELDAR" stand out bigger than the rest of the text.
Nice to have
• Name "VELDAR" can be centered on one side or in the corner or along side edges, just need something cool and different.
Should not have
• I am open just try to keep it clean looking

```html
<!DOCTYPE html>
<html lang="en">
<head>
<meta charset="utf-8">
<title>VELDAR Artist Mgmt. + Design Co. — Business Card</title>
<link href="https://fonts.googleapis.com/css2?family=Arimo:wght@400;700&family=Lato:wght@300;400&display=swap" rel="stylesheet">
<style>
  :root {
    --backdrop: #2b2724;
    --card: #0e0e0e;
    --gold: #a58b4f;
    --bronze: #7a6440;
    --orange: #f37122;
    --blue: #0455a3;
    --silver: #c9cacd;
    --white: #f2f2f2;
    --rule: #3a3a3a;
  }
  * { margin: 0; padding: 0; box-sizing: border-box; }
  html, body {
    width: 1200px; height: 900px; overflow: hidden;
    background: var(--backdrop);
  }
  .canvas {
    position: relative; width: 1200px; height: 900px;
    display: flex; align-items: center; justify-content: center; gap: 50px;
  }
  .card {
    position: relative; width: 525px; height: 300px;
    background: var(--card);
    box-shadow: 0 18px 40px rgba(0,0,0,.45);
  }

  /* Contact side */
  .card--contact { display: flex; align-items: center; }
  .brand-block {
    width: 210px; height: 100%; flex: none;
    display: flex; align-items: center; justify-content: center; gap: 12px;
  }
  .brand-block__square { width: 22px; height: 22px; background: var(--orange); }
  .brand-block__name {
    font-family: "Arimo", Arial, sans-serif; font-weight: 700;
    font-size: 32px; letter-spacing: 1px; color: var(--gold);
  }
  .divider { width: 1px; height: 170px; background: var(--rule); flex: none; }
  .contact { padding-left: 22px; font-family: "Arimo", Arial, sans-serif; color: var(--white); }
  .contact__name {
    font-weight: 700; font-size: 16px; letter-spacing: .3px;
    color: var(--gold); text-transform: uppercase; margin-bottom: 10px;
  }
  .contact__list { list-style: none; }
  .contact__item {
    display: flex; align-items: center; gap: 7px;
    font-size: 14px; line-height: 18px; white-space: nowrap;
  }
  .contact__icon { width: 13px; height: 13px; flex: none; }
  .contact__address { margin-top: 12px; font-size: 14px; line-height: 18px; font-style: normal; }

  /* Brand side */
  .card--brand {
    display: flex; flex-direction: column; align-items: center; justify-content: center;
  }
  .brand-mark { display: flex; align-items: center; gap: 14px; }
  .brand-mark__square { width: 30px; height: 30px; background: var(--orange); }
  .brand-mark__name {
    font-family: "Arimo", Arial, sans-serif; font-weight: 400;
    font-size: 58px; letter-spacing: 1px; color: var(--bronze); line-height: 1;
  }
  .tagline {
    margin-top: 16px;
    font-family: "Lato", Arial, sans-serif; font-weight: 300;
    font-size: 14px; letter-spacing: 3px; color: var(--silver);
    text-transform: uppercase;
  }
  .tagline__pipe { color: var(--blue); font-weight: 400; }
</style>
</head>
<body>
<main class="canvas">
  <section class="card card--contact" aria-label="Business card, contact side">
    <div class="brand-block">
      <span class="brand-block__square"></span>
      <span class="brand-block__name">VELDAR</span>
    </div>
    <div class="divider"></div>
    <div class="contact">
      <h1 class="contact__name">Theodore Quillan</h1>
      <ul class="contact__list">
        <li class="contact__item">
          <svg class="contact__icon" viewBox="0 0 13 13"><rect width="13" height="13" rx="2" fill="var(--gold)"/><path d="M4 3.2l1.4 1.6-.7 1a5 5 0 0 0 2.5 2.5l1-.7 1.6 1.4-.9 1.1C6.2 10 3 6.8 2.9 4.1z" fill="var(--card)"/></svg>
          415.638.2090
        </li>
        <li class="contact__item">
          <svg class="contact__icon" viewBox="0 0 13 13"><rect width="13" height="13" rx="2" fill="var(--gold)"/><path d="M4 3.2l1.4 1.6-.7 1a5 5 0 0 0 2.5 2.5l1-.7 1.6 1.4-.9 1.1C6.2 10 3 6.8 2.9 4.1z" fill="var(--card)"/></svg>
          415.638.2097 (DIRECT)
        </li>
        <li class="contact__item">
          <svg class="contact__icon" viewBox="0 0 13 13"><rect width="13" height="13" rx="2" fill="var(--gold)"/><rect x="3" y="5" width="7" height="5" fill="var(--card)"/><rect x="4.5" y="2.5" width="4" height="3" fill="var(--card)"/></svg>
          415.638.2098
        </li>
        <li class="contact__item">
          <svg class="contact__icon" viewBox="0 0 13 13"><rect width="13" height="13" rx="2" fill="var(--gold)"/><rect x="2.5" y="4" width="8" height="5.5" fill="var(--card)"/><path d="M2.5 4l4 3 4-3" stroke="var(--gold)" fill="none"/></svg>
          veldarartist@mailnest.example
        </li>
        <li class="contact__item">
          <svg class="contact__icon" viewBox="0 0 13 13"><rect width="13" height="13" rx="2" fill="var(--gold)"/><circle cx="6.5" cy="6.5" r="3.6" fill="none" stroke="var(--card)" stroke-width="1.2"/><path d="M2.9 6.5h7.2M6.5 2.9v7.2" stroke="var(--card)"/></svg>
          www.veldarart.example
        </li>
      </ul>
      <address class="contact__address">
        2416 Harrowgate Ave. #317<br>Miami, Florida 33152
      </address>
    </div>
  </section>

  <section class="card card--brand" aria-label="Business card, brand side">
    <div class="brand-mark">
      <span class="brand-mark__square"></span>
      <span class="brand-mark__name">VELDAR</span>
    </div>
    <p class="tagline">Artist Management <span class="tagline__pipe">|</span> Design Co</p>
  </section>
</main>
</body>
</html>
```